Vantrel Ashcombe LLC

we need a business card design

Industry/Entity Type

hvac

Contact Information for Business Card

my logo

Requirements
Must have
• my logo and same colors

```html
<!DOCTYPE html>
<html lang="en">
<head>
<meta charset="utf-8">
<title>Vantrel Ashcombe LLC – Business Card</title>
<link rel="stylesheet" href="https://fonts.googleapis.com/css2?family=Poppins:wght@400;500;700&display=swap">
<style>
  :root {
    --brand-blue: #1456a8;
    --brand-blue-dark: #0f4a94;
    --ink: #1f1f1f;
    --card-white: #ffffff;
    --backdrop: #e6e6e6;
  }
  * { box-sizing: border-box; margin: 0; padding: 0; }
  html, body {
    width: 1200px;
    height: 773px;
    overflow: hidden;
    background: var(--backdrop);
    font-family: "Poppins", sans-serif;
  }
  .business-card {
    position: absolute;
    left: 150px;
    top: 130px;
    width: 900px;
    height: 514px;
    background: var(--card-white);
    box-shadow: 0 10px 30px rgba(0,0,0,0.12);
  }
  .brand-mark {
    position: absolute;
    right: 90px;
    top: 90px;
    display: flex;
    align-items: center;
    gap: 14px;
  }
  .brand-mark__dot {
    width: 34px;
    height: 34px;
    border-radius: 50%;
    background: var(--brand-blue);
  }
  .brand-mark__name {
    font-weight: 700;
    font-size: 30px;
    color: var(--brand-blue);
    letter-spacing: 0.5px;
  }
  .accent-bar {
    position: absolute;
    left: 0;
    top: 250px;
    width: 14px;
    height: 88px;
    background: var(--brand-blue);
  }
  .holder {
    position: absolute;
    left: 52px;
    top: 246px;
  }
  .holder__name {
    font-weight: 700;
    font-size: 42px;
    line-height: 1.1;
    color: var(--brand-blue-dark);
    letter-spacing: 0.5px;
  }
  .holder__title {
    font-size: 22px;
    color: var(--ink);
    margin-top: 2px;
  }
  .divider {
    position: absolute;
    left: 80px;
    right: 80px;
    top: 352px;
    height: 2px;
    background: var(--brand-blue);
  }
  .contact-list {
    position: absolute;
    left: 92px;
    top: 372px;
    list-style: none;
  }
  .contact-list__item {
    display: flex;
    align-items: center;
    gap: 14px;
    font-size: 21px;
    line-height: 34px;
    color: var(--ink);
  }
  .contact-list__icon {
    width: 18px;
    height: 18px;
    fill: var(--brand-blue);
    flex: none;
  }
  .company-address {
    position: absolute;
    right: 80px;
    top: 380px;
    text-align: right;
    color: var(--ink);
  }
  .company-address__name {
    font-weight: 500;
    font-size: 21px;
  }
  .company-address__city {
    font-size: 19px;
  }
</style>
</head>
<body>
  <article class="business-card">
    <div class="brand-mark">
      <span class="brand-mark__dot"></span>
      <span class="brand-mark__name">Vantrel Ashcombe LLC</span>
    </div>

    <span class="accent-bar"></span>
    <div class="holder">
      <h1 class="holder__name">DORIAN KESSLING</h1>
      <p class="holder__title">Managing Director</p>
    </div>

    <span class="divider"></span>

    <ul class="contact-list">
      <li class="contact-list__item">
        <svg class="contact-list__icon" viewBox="0 0 24 24" aria-hidden="true"><path d="M6.6 10.8a15.1 15.1 0 0 0 6.6 6.6l2.2-2.2a1 1 0 0 1 1-.25 11.4 11.4 0 0 0 3.6.57 1 1 0 0 1 1 1V20a1 1 0 0 1-1 1A17 17 0 0 1 3 4a1 1 0 0 1 1-1h3.5a1 1 0 0 1 1 1c0 1.25.2 2.45.57 3.57a1 1 0 0 1-.25 1z"/></svg>
        +1 555-013-2740
      </li>
      <li class="contact-list__item">
        <svg class="contact-list__icon" viewBox="0 0 24 24" aria-hidden="true"><path d="M2 5h20v14H2z M2 5l10 8 10-8" /><path d="M3 6l9 7 9-7v2l-9 7-9-7z" fill="#fff"/></svg>
        mara@vantrelairservice.com
      </li>
      <li class="contact-list__item">
        <svg class="contact-list__icon" viewBox="0 0 24 24" aria-hidden="true"><circle cx="12" cy="12" r="10"/><path d="M7 7c2 1 3 3 2 5s1 3 3 3M14 4c0 2 2 3 4 3M15 20c0-2 1-3 3-3" stroke="#fff" stroke-width="1.6" fill="none"/></svg>
        www.vantrelashcombe.com
      </li>
    </ul>

    <address class="company-address">
      <p class="company-address__name">Vantrel Ashcombe</p>
      <p class="company-address__city">Harlow Point, FL, USA</p>
    </address>
  </article>
</body>
</html>
```